Cookie Bakery : need logo andbusiness cards

Don't want anything cartoonish. Business name "Hollow Oven Treats"

I am starting a cookie business. It is not store front business, will be selling at local farmers market. Looking to market toward businesses, people needing desserts for parties, etc. Hope this helps, kinda wanting to get "logo brand" nailed, then follow up with info to be printed on card.

Industry/Entity Type

Store

Font styles to use
Decorative

Requirements
Should not have
• Don't want anything cartoonish

```html
<!DOCTYPE html>
<html lang="en">
<head>
<meta charset="utf-8">
<title>Hollow Oven Treats — Business Card</title>
<link rel="stylesheet" href="https://fonts.googleapis.com/css2?family=Exo+2:wght@400;600;800&family=Oswald:wght@400&display=swap">
<style>
  :root {
    --stage: #1a1a1a;
    --card: #262626;
    --card-edge: #303030;
    --brand-red: #d7272f;
    --deep-red: #b01c24;
    --band-grey: #6b6b6b;
    --ink-light: #f2f2f2;
    --ink-muted: #c9c9c9;
  }
  * { margin: 0; padding: 0; box-sizing: border-box; }
  html, body { width: 1200px; height: 864px; overflow: hidden; background: var(--stage); }
  .canvas {
    position: relative; width: 1200px; height: 864px;
    display: flex; flex-direction: column; align-items: center; justify-content: center; gap: 32px;
  }
  .card {
    position: relative; width: 640px; height: 366px;
    background: var(--card);
    box-shadow: 0 0 0 1px var(--card-edge);
    overflow: hidden;
    font-family: "Exo 2", sans-serif;
  }
  .brand-name {
    font-family: "Exo 2", sans-serif; font-weight: 800; color: var(--brand-red);
    letter-spacing: 0.5px; white-space: nowrap;
  }
  .card-front .brand-name {
    position: absolute; top: 50%; left: 50%; transform: translate(-50%, -50%);
    font-size: 46px;
  }
  .card-back .brand-name {
    position: absolute; top: 98px; right: 36px; font-size: 34px;
  }
  .card-back .band { position: absolute; left: 0; bottom: 0; width: 640px; height: 150px; }
  .address {
    position: absolute; right: 26px; bottom: 54px;
    color: var(--ink-light); font-size: 14px; font-weight: 600; letter-spacing: 0.3px;
  }
  .person { position: absolute; left: 30px; top: 184px; color: var(--ink-light); }
  .person-name { font-family: "Oswald", sans-serif; font-size: 22px; letter-spacing: 1px; line-height: 1; }
  .person-role { font-size: 10px; letter-spacing: 1.5px; margin-top: 4px; color: var(--ink-muted); }
  .contacts { position: absolute; left: 30px; top: 238px; list-style: none; }
  .contacts li {
    display: flex; align-items: center; gap: 8px;
    font-size: 10px; color: var(--ink-muted); height: 16px;
  }
  .contacts svg { width: 10px; height: 10px; fill: var(--ink-light); flex: none; }
</style>
</head>
<body>
<main class="canvas">
  <section class="card card-front">
    <div class="brand-name">Hollow Oven Treats</div>
  </section>

  <section class="card card-back">
    <div class="brand-name">Hollow Oven Treats</div>

    <svg class="band" viewBox="0 0 640 150" aria-hidden="true">
      <path d="M0 126 H336 C350 126 352 104 368 104 H640 V150 H0 Z" fill="var(--band-grey)"/>
      <path d="M0 134 H340 C354 134 356 112 372 112 H640 V150 H0 Z" fill="var(--brand-red)"/>
      <path d="M0 142 H640 V150 H0 Z" fill="var(--deep-red)"/>
    </svg>
    <div class="address">42 Mill Lane, 3rd Floor, Riverside</div>

    <div class="person">
      <div class="person-name">DANA REYES</div>
      <div class="person-role">GENERAL MANAGER</div>
    </div>

    <ul class="contacts">
      <li><svg viewBox="0 0 10 10"><path d="M2 0 L4 2.5 L3 3.6 Q4.5 6 6.4 7 L7.5 6 L10 8 L8.6 9.6 Q3.5 9 0.4 1.4 Z"/></svg>555 014 2290</li>
      <li><svg viewBox="0 0 10 10"><path d="M2.5 0 H7.5 V10 H2.5 Z M3.3 1 V8 H6.7 V1 Z"/></svg>555 014 2291</li>
      <li><svg viewBox="0 0 10 10"><path d="M2 0 H7 V3 H9 V8 H1 V3 H2 Z M3 1 V3 H6 V1 Z M2 8.5 H8 V10 H2 Z"/></svg>555 014 2292</li>
      <li><svg viewBox="0 0 10 10"><path d="M0 2 H10 V8 H0 Z M0.8 2.6 L5 5.6 L9.2 2.6"/></svg>hello@hollowoven.com</li>
      <li><svg viewBox="0 0 10 10"><circle cx="5" cy="5" r="4.6"/></svg>www.hollowoven.com</li>
    </ul>
  </section>
</main>
</body>
</html>
```